Business Cards and Stationary for telecommunications application
BrightOak Ventures
Business Cards and Stationary for telecommunications application - Telecommunications
Creative Brief
Simple
Louis Merrow
President
20391 Kelvane Court Fenwick Hollow, NV
louis@brightoakventures.com
brightoakventures.com

```html
<!DOCTYPE html>
<html lang="en">
<head>
<meta charset="utf-8">
<title>BrightOak Ventures – Business Cards</title>
<link href="https://fonts.googleapis.com/css2?family=Open+Sans:ital,wght@0,400;0,600;0,700;1,400;1,600&display=swap" rel="stylesheet">
<style>
  :root {
    --backdrop: #d9d9d9;
    --paper: #ffffff;
    --brand-red: #b5121b;
    --deep-red: #8c0d13;
    --ink: #1d1d1d;
    --swoosh-grey: #9a9a9a;
    --light-text: #ffffff;
  }
  * { margin: 0; padding: 0; box-sizing: border-box; }
  html, body {
    width: 1200px; height: 895px; overflow: hidden;
    background: var(--backdrop);
    font-family: "Open Sans", Arial, sans-serif;
  }
  .canvas {
    position: relative; width: 1200px; height: 895px;
    display: flex; flex-direction: column; align-items: center;
    justify-content: center; gap: 36px;
  }
  .card {
    position: relative; width: 700px; height: 400px;
    background: var(--paper); overflow: hidden;
    box-shadow: 0 6px 18px rgba(0,0,0,0.18);
  }
  .brand {
    display: flex; align-items: center; gap: 14px;
    position: absolute;
  }
  .brand-dot {
    width: 54px; height: 54px; border-radius: 50%;
    background: var(--brand-red);
  }
  .brand-name {
    font-weight: 600; font-size: 34px; color: var(--brand-red);
    letter-spacing: 0.5px; white-space: nowrap;
  }
  /* back of card */
  .card-back .brand { left: 90px; top: 70px; }
  .card-back .web {
    position: absolute; right: 48px; bottom: 58px;
    font-style: italic; font-size: 21px; letter-spacing: 5px;
    color: var(--deep-red); white-space: nowrap;
  }
  /* front of card */
  .card-front .brand { left: 60px; top: 48px; }
  .front-wave { position: absolute; left: 0; top: 0; width: 700px; height: 400px; }
  .front-info {
    position: absolute; left: 0; right: 0; top: 225px; bottom: 0;
    color: var(--light-text);
  }
  .address {
    position: absolute; left: 40px; top: 58px;
    font-size: 14px; line-height: 1.55; white-space: nowrap;
  }
  .person { position: absolute; left: 285px; top: 30px; }
  .person-name { font-size: 18px; font-weight: 700; white-space: nowrap; }
  .person-title { font-size: 13px; font-style: italic; }
  .contacts {
    position: absolute; left: 440px; top: 58px;
    list-style: none; font-size: 13px; line-height: 1.9;
  }
  .contacts li { display: flex; align-items: center; gap: 8px; white-space: nowrap; }
  .contacts svg { width: 14px; height: 14px; flex: none; }
</style>
</head>
<body>
<main class="canvas">
  <section class="card card-back">
    <div class="brand">
      <span class="brand-dot"></span>
      <span class="brand-name">BrightOak Ventures</span>
    </div>
    <p class="web">www.brightoakventures.com</p>
  </section>

  <section class="card card-front">
    <svg class="front-wave" viewBox="0 0 700 400" preserveAspectRatio="none" aria-hidden="true">
      <defs>
        <linearGradient id="redFill" x1="0" y1="0" x2="0" y2="1">
          <stop offset="0" stop-color="#c8141e"/>
          <stop offset="1" stop-color="#8c0d13"/>
        </linearGradient>
      </defs>
      <path d="M0 170 C 200 150, 420 230, 700 160 L700 400 L0 400 Z" fill="#9a9a9a"/>
      <path d="M0 180 C 200 162, 420 242, 700 172 L700 400 L0 400 Z" fill="#1d1d1d"/>
      <path d="M0 196 C 200 178, 420 258, 700 188 L700 400 L0 400 Z" fill="url(#redFill)"/>
    </svg>
    <div class="brand">
      <span class="brand-dot"></span>
      <span class="brand-name">BrightOak Ventures</span>
    </div>
    <div class="front-info">
      <p class="address">20391 Kelvane Court<br>Fenwick Hollow, NV</p>
      <div class="person">
        <p class="person-name">Louis Merrow</p>
        <p class="person-title">President</p>
      </div>
      <ul class="contacts">
        <li>
          <svg viewBox="0 0 14 14"><circle cx="7" cy="7" r="7" fill="#fff"/><path d="M4.5 3.5h1.6l.6 2-1 .8a5 5 0 0 0 2 2l.8-1 2 .6v1.6c0 .4-.4.8-.8.8A6.2 6.2 0 0 1 3.7 4.3c0-.4.4-.8.8-.8z" fill="#b5121b"/></svg>
          555-014-2280
        </li>
        <li>
          <svg viewBox="0 0 14 14"><circle cx="7" cy="7" r="7" fill="#fff"/><rect x="3.5" y="4.5" width="7" height="5" fill="none" stroke="#b5121b"/><path d="M3.5 4.5 7 7.3l3.5-2.8" fill="none" stroke="#b5121b"/></svg>
          louis@brightoakventures.com
        </li>
        <li>
          <svg viewBox="0 0 14 14"><circle cx="7" cy="7" r="7" fill="#fff"/><circle cx="7" cy="7" r="3.6" fill="none" stroke="#b5121b"/><path d="M3.4 7h7.2M7 3.4v7.2" stroke="#b5121b"/></svg>
          www.brightoakventures.com
        </li>
      </ul>
    </div>
  </section>
</main>
</body>
</html>
```